Brenvick Holdings LLC, new Business cards

I'm moving offices and need new cards. Plus I'm open to modifying the current design of my card. I will keep the logo but would like to explore other layouts and fonts for the design. I've included the current double sided card for reference. I Like the navy color and white. Might be open to grays or silver. Needs to be clean and elegant.

Target Market(s)

Investors, buyers & sellers of private equities and real estate.

Contact Information for Business Card

Brenvick Holdings
Dorian P.K. Halvers, Managing Principal
418 Ostrander Ave., Suite 612
Denver, CO 80319
M: 970-555-0147, O: 303-555-0192
Dorian@brenvickholdings.example
Brenvickholdings.example

Colors
0354a2
ffffff
c4c4c4

Requirements
Must have
• Business card details.
• Logo raised or embossed, it was designed after a wax seal. Current has raised ink.
Nice to have
• Space on card to write additional notes.

```html
<!DOCTYPE html>
<html lang="en">
<head>
<meta charset="utf-8">
<title>Brenvick Holdings — Business Card</title>
<link href="https://fonts.googleapis.com/css2?family=Roboto:wght@400;500;700&display=swap" rel="stylesheet">
<style>
  :root {
    --navy: #2b2660;
    --navy-deep: #221e4f;
    --paper: #ececec;
    --silver: #c4c4c4;
    --slate: #6e6e6e;
    --ink: #222;
    --backdrop: #3a3a3a;
  }
  * { box-sizing: border-box; margin: 0; padding: 0; }
  html, body { width: 1200px; height: 1000px; overflow: hidden; }
  body {
    background: var(--backdrop);
    font-family: "Roboto", Arial, sans-serif;
    position: relative;
  }
  .card {
    position: absolute;
    left: 250px;
    width: 700px;
    height: 400px;
    border-radius: 22px;
    overflow: hidden;
  }
  /* Back side */
  .card--back {
    top: 50px;
    background: var(--slate);
    display: flex;
    align-items: center;
    justify-content: center;
  }
  .brand {
    display: flex;
    align-items: center;
    gap: 18px;
  }
  .brand__dot {
    width: 64px; height: 64px;
    border-radius: 50%;
    background: var(--navy);
  }
  .brand__name {
    font-weight: 700;
    font-size: 30px;
    letter-spacing: 3px;
    text-transform: uppercase;
    color: #ffffff;
  }
  .card--back .brand__name { color: #f2f2f2; }

  /* Front side */
  .card--front {
    top: 520px;
    background: var(--paper);
  }
  .card--front .brand {
    position: absolute;
    top: 40px; left: 40px;
  }
  .card--front .brand__name { color: var(--navy); font-size: 26px; }
  .watermark {
    position: absolute;
    right: -40px; top: 150px;
    width: 280px; height: 280px;
    border-radius: 50%;
    background: #dedede;
  }
  .rule {
    position: absolute;
    left: 40px; top: 180px;
    width: 430px; height: 2px;
    background: var(--ink);
  }
  .contact {
    position: absolute;
    left: 40px; top: 200px;
    list-style: none;
    font-size: 15px;
    color: var(--ink);
    line-height: 26px;
  }
  .contact li { display: flex; align-items: center; gap: 8px; }
  .contact svg { width: 14px; height: 14px; fill: var(--navy); flex: none; }
  .person {
    position: absolute;
    right: 40px; top: 188px;
    text-align: right;
  }
  .person__name {
    font-weight: 700;
    font-size: 24px;
    color: var(--navy);
  }
  .person__title {
    font-size: 15px;
    color: #444;
    margin-top: 4px;
    padding-top: 4px;
    border-top: 2px solid var(--ink);
  }
  .person__address {
    font-size: 16px;
    color: #333;
    margin-top: 10px;
    line-height: 21px;
  }
  .base {
    position: absolute;
    left: 0; bottom: 0;
    width: 700px; height: 56px;
  }
</style>
</head>
<body>
  <section class="card card--back" aria-label="Card back">
    <div class="brand">
      <span class="brand__dot"></span>
      <span class="brand__name">Brenvick Holdings</span>
    </div>
  </section>

  <section class="card card--front" aria-label="Card front">
    <div class="watermark"></div>
    <div class="brand">
      <span class="brand__dot"></span>
      <span class="brand__name">Brenvick Holdings</span>
    </div>
    <div class="rule"></div>
    <ul class="contact">
      <li><svg viewBox="0 0 24 24"><path d="M6.6 10.8a15.1 15.1 0 0 0 6.6 6.6l2.2-2.2a1 1 0 0 1 1-.25 11.4 11.4 0 0 0 3.6.57 1 1 0 0 1 1 1V20a1 1 0 0 1-1 1A17 17 0 0 1 3 4a1 1 0 0 1 1-1h3.5a1 1 0 0 1 1 1c0 1.25.2 2.45.57 3.6a1 1 0 0 1-.25 1z"/></svg>970-555-0147, O: TBD</li>
      <li><svg viewBox="0 0 24 24"><path d="M2 5h20v14H2zm2 2v.5l8 5 8-5V7z"/></svg>dorian@brenvickholdings.example</li>
      <li><svg viewBox="0 0 24 24"><path d="M12 2a10 10 0 1 0 0 20 10 10 0 0 0 0-20zm-1 2.1V8H7.3A8 8 0 0 1 11 4.1zM13 4.1A8 8 0 0 1 16.7 8H13zM4.3 10H11v4H4.3a8 8 0 0 1 0-4zm8.7 0h6.7a8 8 0 0 1 0 4H13zm-5.7 6H11v3.9A8 8 0 0 1 7.3 16zm5.7 0h3.7a8 8 0 0 1-3.7 3.9z"/></svg>www.brenvickholdings.example</li>
    </ul>
    <div class="person">
      <div class="person__name">Dorian P.K. Halvers</div>
      <div class="person__title">Managing Principal</div>
      <div class="person__address">418 Ostrander Ave., Suite 612<br>Denver, CO 80319</div>
    </div>
    <svg class="base" viewBox="0 0 700 56" aria-hidden="true">
      <rect x="0" y="22" width="700" height="34" fill="var(--navy-deep)"/>
      <path d="M0 0 H300 Q315 0 322 12 Q330 22 345 22 H0 Z" fill="var(--silver)"/>
    </svg>
  </section>
</body>
</html>
```